specialised legal consultancy business needs an update on logo and office stationary.

Update on Logo - see attached.

update on email signature - something new and fresh with only the following details -

(the logo)
Advocate Peter Sandovik
PS Entity Frameworks (Pty) Ltd (Reg No.: 2019 / 153927 / 07)
LLB, LLM (Cum Laude), Cert.Dir (KWBFE), FCG (TREPX)
+27 71 592 6604
peter#kwellbrandt.com

Update on letterhead - something new and fresh and please more user-friendly. With the same details as per the email signature.

```html
<!DOCTYPE html>
<html lang="en">
<head>
<meta charset="utf-8">
<title>PS Entity Frameworks – Letterhead</title>
<link rel="stylesheet" href="https://fonts.googleapis.com/css2?family=Open+Sans:wght@400&family=Roboto:wght@400;500&display=swap">
<style>
  :root {
    --backdrop: #dedede;
    --paper: #f8f8f8;
    --ink-strong: #111111;
    --ink-body: #666666;
    --ink-header: #555555;
    --signature-tone: #dfe3ea;
  }
  * { margin: 0; padding: 0; box-sizing: border-box; }
  html, body {
    width: 1153px; height: 1200px; overflow: hidden;
    background: var(--backdrop);
  }
  .letterhead {
    position: absolute; left: 167px; top: 30px;
    width: 818px; height: 1140px;
    background: var(--paper);
  }
  .brand {
    position: absolute; left: 72px; top: 150px;
    display: flex; align-items: center; gap: 10px;
  }
  .brand-mark { width: 14px; height: 14px; background: var(--ink-strong); }
  .brand-name {
    font-family: "Roboto", sans-serif; font-weight: 500;
    font-size: 15px; letter-spacing: 2px; color: var(--ink-strong);
  }
  .company-details {
    position: absolute; left: 503px; top: 88px; width: 240px;
    font-family: "Roboto", sans-serif; font-size: 14.6px;
    color: var(--ink-header); line-height: 19px;
  }
  .company-name { color: var(--ink-strong); font-weight: 500; }
  .company-address { margin-top: 6px; }
  .contact-line { display: flex; align-items: center; gap: 4px; margin-top: 3px; }
  .company-address + .contact-line { margin-top: 6px; }
  .contact-icon { width: 14px; height: 12px; fill: var(--ink-strong); }
  .letter-body {
    position: absolute; left: 72px; top: 293px; width: 670px;
    font-family: "Open Sans", sans-serif; font-size: 14.6px;
    line-height: 21.9px; color: var(--ink-body);
  }
  .letter-body p { text-align: justify; margin-bottom: 22px; }
  .letter-body .salutation { margin-bottom: 22px; }
  .signature-area {
    position: absolute; left: 72px; top: 870px;
    width: 97px; height: 90px; background: var(--signature-tone);
  }
  .credentials {
    position: absolute; left: 0; top: 1052px; width: 818px;
    text-align: center; font-family: "Roboto", sans-serif;
    font-size: 13px; line-height: 23px; color: var(--ink-header);
  }
  .credentials .divider { color: var(--ink-strong); font-weight: 500; margin: 0 4px; }
</style>
</head>
<body>
  <main class="letterhead">
    <div class="brand">
      <span class="brand-mark"></span>
      <span class="brand-name">PS ENTITY FRAMEWORKS</span>
    </div>

    <address class="company-details" style="font-style:normal">
      <div class="company-name">PS Entity Frameworks (Pty) Ltd</div>
      <div>Reg No.: 2019 / 153927 / 07</div>
      <div class="company-address">214 Lindenhof Avenue,<br>Waterkloof Glen, Pretoria</div>
      <div class="contact-line">
        <svg class="contact-icon" viewBox="0 0 14 12" aria-hidden="true"><path d="M1 4c0-2 3-3 6-3s6 1 6 3v1h-3V4H4v1H1zM3 6h8l2 5H1z"/></svg>
        <span>+27 71 592 6604</span>
      </div>
      <div class="contact-line">
        <svg class="contact-icon" viewBox="0 0 14 12" aria-hidden="true"><path d="M0 1h14v10H0zM1.5 2.5v7h11v-7L7 7z" fill-rule="evenodd"/></svg>
        <span>peter#kwellbrandt.com</span>
      </div>
    </address>

    <article class="letter-body">
      <p class="salutation">Dear customer,</p>
      <p>Lorem ipsum dolor sit amet, consectetur adipisicing elit, sed do eiusmod tempor incididunt ut labore et dolore magna aliqua. Ut enim ad minim veniam, quis nostrud exercitation ullamco laboris nisi ut aliquip ex ea commodo consequat. Duis aute irure dolor in reprehenderit in voluptate velit esse cillum dolore eu fugiat nulla pariatur. Excepteur sint occaecat cupidatat non proident, sunt in culpa qui officia deserunt mollit anim id est laborum.</p>
      <p>Lorem ipsum dolor sit amet, consectetur adipisicing elit, sed do eiusmod tempor incididunt ut labore et dolore magna aliqua. Ut enim ad minim veniam, quis nostrud exercitation ullamco laboris nisi ut aliquip ex ea commodo consequat. Duis aute irure dolor in reprehenderit in voluptate velit esse cillum dolore eu fugiat nulla pariatur. Excepteur sint occaecat cupidatat non proident, sunt in culpa qui officia deserunt mollit anim id est laborum.</p>
      <p>Lorem ipsum dolor sit amet, consectetur adipisicing elit, sed do eiusmod tempor incididunt ut labore et dolore magna aliqua. Ut enim ad minim veniam, quis nostrud exercitation ullamco laboris nisi ut aliquip ex ea commodo consequat. Duis aute irure dolor in reprehenderit in voluptate velit esse cillum dolore eu fugiat nulla pariatur. Excepteur sint occaecat cupidatat non proident, sunt in culpa qui officia deserunt mollit anim id est laborum.</p>
      <p>Lorem ipsum dolor sit amet, consectetur adipisicing elit, sed do eiusmod tempor incididunt ut labore et dolore magna aliqua. Ut enim ad minim veniam, quis nostrud exercitation ullamco laboris nisi ut aliquip ex ea commodo consequat. Duis aute irure dolor in reprehenderit.</p>
      <p class="closing">Yours Sincerely,</p>
    </article>

    <div class="signature-area" role="img" aria-label="Handwritten signature of Peter Sandovik"></div>

    <footer class="credentials">
      <div>Advocate of the High Court<span class="divider">|</span>Mediator<span class="divider">|</span>Arbitrator<span class="divider">|</span>LLB, LLM (Cum Laude)<span class="divider">|</span>Cert.Dir (KWBFE), FCG (TREPX)</div>
      <div>Chartered Secretary (TREPX)<span class="divider">|</span>Member of In-House Counsel Forum of South Africa</div>
    </footer>
  </main>
</body>
</html>
```